Banner Design Project – Commercial & Residential Pest Control

The large 4' x 6' banner should attract commercial customers and emphasize our expertise in bed bug control, risk management, and commercial pest management.

The 3–4 smaller residential banners should work together to showcase the range of pest control services we offer homeowners, including general pest control, gopher and vole control, and mouse control.

Across the entire set, we want customers to understand that they are dealing with an experienced, professional, locally owned and operated family business that has been serving the community since 2017.

Details are in attached PDF. I also included pictures of our new trade show backdrop and current pictures of the area we are working in the banners will be on either wall NOT the back. The tables will remain. I have included a lot of our information and pictures to get an idea of the company.

```html
<!DOCTYPE html>
<html lang="en">
<head>
<meta charset="UTF-8">
<title>Ridgeline Pest Control – Duct & Dryer Vent Cleaning</title>
<link rel="stylesheet" href="https://fonts.googleapis.com/css2?family=Anton&family=Roboto+Condensed:wght@500;700;800&display=swap">
<style>
  :root {
    --orange: #f26a1b;
    --orange-deep: #d9520c;
    --ink: #141414;
    --row: #232323;
    --row-edge: #3a3a3a;
    --white: #ffffff;
  }
  * { margin: 0; padding: 0; box-sizing: border-box; }
  html, body { width: 774px; height: 1200px; overflow: hidden; background: var(--ink); }
  .banner {
    position: relative;
    width: 774px;
    height: 1200px;
    overflow: hidden;
    background: var(--ink);
    font-family: "Roboto Condensed", sans-serif;
    color: var(--white);
  }
  .hero-photo {
    position: absolute;
    left: 0; top: 0;
    width: 774px; height: 600px;
    background:
      radial-gradient(ellipse at 62% 20%, #f4f2ee 0%, #dcd8d1 45%, transparent 70%),
      radial-gradient(ellipse at 25% 40%, rgba(242,106,27,0.55) 0%, transparent 35%),
      linear-gradient(180deg, #ebe8e3 0%, #cfc9bf 60%, #b9b1a5 100%);
  }
  .brand {
    position: absolute;
    left: 28px; top: 30px;
    display: flex; align-items: center; gap: 10px;
    font-weight: 800;
    font-size: 34px;
    color: var(--orange);
    letter-spacing: 0.5px;
  }
  .brand-mark { width: 22px; height: 22px; background: var(--orange); }
  .tag-series {
    position: absolute;
    right: 26px; top: 31px;
    width: 237px; height: 46px;
    background: var(--orange);
    border-radius: 4px;
    font-weight: 800; font-size: 21px;
    letter-spacing: 1.5px;
    display: flex; align-items: center; justify-content: center;
  }
  .tag-local {
    position: absolute;
    right: 26px; top: 93px;
    width: 237px; height: 113px;
    background: rgba(20,20,20,0.92);
    border-radius: 4px;
    text-align: center;
    font-weight: 700; font-size: 17px;
    line-height: 1.4;
    letter-spacing: 1px;
    padding-top: 20px;
  }
  .tag-local .since { color: var(--orange); display: block; margin-top: 4px; }
  .divider { position: absolute; left: 0; top: 440px; width: 774px; height: 170px; }
  .headline {
    position: absolute;
    left: 44px; top: 596px;
    font-family: "Anton", sans-serif;
    font-weight: 400;
    font-size: 70px;
    line-height: 1.06;
    letter-spacing: 5px;
    text-transform: uppercase;
  }
  .headline .accent { color: var(--orange); display: block; }
  .benefits {
    position: absolute;
    left: 39px; top: 764px;
    width: 691px;
    list-style: none;
  }
  .benefit {
    display: flex; align-items: center;
    height: 66px;
    margin-bottom: 18px;
    background: var(--row);
    border: 1px solid var(--row-edge);
    border-radius: 6px;
    overflow: hidden;
  }
  .benefit-num {
    width: 70px; height: 100%;
    background: var(--orange);
    display: flex; align-items: center; justify-content: center;
    font-weight: 800; font-size: 26px;
  }
  .benefit-text {
    flex: 1;
    padding-left: 22px;
    font-weight: 700; font-size: 25px;
  }
  .benefit-dash {
    width: 34px; height: 4px;
    background: var(--orange);
    margin-right: 26px;
    border-radius: 2px;
  }
  .footer-panel { position: absolute; left: 0; top: 1104px; width: 420px; height: 96px; }
  .footer-tagline {
    position: absolute;
    left: 28px; top: 1114px;
    font-weight: 700; font-size: 17px;
    letter-spacing: 1.5px;
    color: var(--white);
  }
  .phone {
    position: absolute;
    left: 24px; top: 1140px;
    display: flex; align-items: center; gap: 10px;
    font-weight: 800; font-size: 42px;
    letter-spacing: 1px;
  }
  .web {
    position: absolute;
    right: 30px; top: 1130px;
    font-weight: 800; font-size: 32px;
    letter-spacing: 1.5px;
  }
</style>
</head>
<body>
<main class="banner">
  <div class="hero-photo" role="img" aria-label="Technician in an orange shirt and gloves feeding a cleaning hose into a ceiling air vent in a bright living room"></div>

  <div class="brand"><span class="brand-mark"></span>Ridgeline</div>

  <div class="tag-series">RESIDENTIAL • 03</div>
  <div class="tag-local">LOCALLY OWNED<br>+ OPERATED<span class="since">SERVING SINCE 2017</span></div>

  <svg class="divider" viewBox="0 0 774 170" preserveAspectRatio="none" aria-hidden="true">
    <polygon points="0,115 774,40 774,170 0,170" fill="#141414"/>
    <polygon points="0,100 774,22 774,36 0,115" fill="#f26a1b"/>
    <polygon points="420,78 774,42 774,54 420,90" fill="#d9520c"/>
  </svg>

  <h1 class="headline">Duct &amp; Dryer<span class="accent">Vent Cleaning</span></h1>

  <ul class="benefits">
    <li class="benefit"><span class="benefit-num">01</span><span class="benefit-text">Improves indoor air quality</span><span class="benefit-dash"></span></li>
    <li class="benefit"><span class="benefit-num">02</span><span class="benefit-text">Prevents dangerous house fires</span><span class="benefit-dash"></span></li>
    <li class="benefit"><span class="benefit-num">03</span><span class="benefit-text">Boosts HVAC and appliance efficiency</span><span class="benefit-dash"></span></li>
    <li class="benefit"><span class="benefit-num">04</span><span class="benefit-text">Lowers utility bills</span><span class="benefit-dash"></span></li>
  </ul>

  <svg class="footer-panel" viewBox="0 0 420 96" preserveAspectRatio="none" aria-hidden="true">
    <polygon points="0,0 380,0 420,96 0,96" fill="#f26a1b"/>
  </svg>
  <p class="footer-tagline">LOCAL FAMILY SERVICE • SINCE 2017</p>
  <p class="phone">
    <svg width="32" height="32" viewBox="0 0 24 24" aria-hidden="true"><path fill="#ffffff" d="M6.6 10.8a15.1 15.1 0 0 0 6.6 6.6l2.2-2.2c.3-.3.7-.4 1-.2 1.1.4 2.3.6 3.6.6.6 0 1 .4 1 1V20c0 .6-.4 1-1 1C10.6 21 3 13.4 3 4c0-.6.4-1 1-1h3.5c.6 0 1 .4 1 1 0 1.3.2 2.5.6 3.6.1.3 0 .7-.2 1z"/></svg>
    208-555-0147
  </p>
  <p class="web">RIDGELINEPEST.COM</p>
</main>
</body>
</html>
```